Strategic Objective - Internal

Take text supplied in a word document and make a stylish, professional document using elements of our brand .This is an internal document for presentation to our small team . Have attached an example document - please do not copy this - this is just to give you the concept. I would like to be able to edit the text in the document you supply back to me also (In word or photoshop)

Our website is www.harrowvt.com.au

Have attached out logo
Thank you

Target Market(s)

Our staff

Industry/Entity Type

Mining, Earthmoving

Requirements
Must have
• Professional, stylish presentation
Nice to have
• Our market includes Australia, Papua New Guinea and teh South Pacific - any graphic that supports this. We are an importer and exporter - any graphics that support this.

```html
<!DOCTYPE html>
<html lang="en">
<head>
<meta charset="utf-8">
<title>Harrow VT – 2024-2025 Financial Year</title>
<link href="https://fonts.googleapis.com/css2?family=Montserrat:wght@300;400;800;900&display=swap" rel="stylesheet">
<style>
  :root {
    --brand-blue: #2a57a4;
    --band-blue: #95abd2;
    --band-overlap: #8ea6cc;
    --panel-grey: #f2f2f2;
    --ink: #474747;
    --accent-green: #8dc54f;
    --paper: #fdfdfd;
  }
  html, body { margin: 0; padding: 0; overflow: hidden; }
  body { background: var(--paper); }
  .sheet {
    position: relative; width: 849px; height: 1200px; overflow: hidden;
    background: var(--paper); font-family: 'Montserrat', sans-serif;
  }
  .sheet svg { position: absolute; inset: 0; }
  .brand-name { font-weight: 900; fill: var(--brand-blue); }
  .brand-dot { fill: var(--accent-green); }
  .panel-grey { fill: var(--panel-grey); }
  .band { fill: var(--band-blue); }
  .band-overlap { fill: var(--band-overlap); }
  .title-years { font-weight: 800; fill: #fff; }
  .title-financial { font-weight: 300; fill: #fff; }
  .title-year { font-weight: 900; fill: #fff; }
  .stat-disc { fill: var(--brand-blue); }
  .stat-ring { fill: none; stroke: var(--brand-blue); stroke-width: 1.3; stroke-dasharray: 4 3; }
  .stat-value { font-weight: 900; fill: #fff; text-anchor: middle; }
  .stat-light { font-weight: 400; fill: var(--ink); text-anchor: middle; }
  .stat-bold { font-weight: 900; fill: var(--ink); text-anchor: middle; }
  .corner-light { fill: var(--band-blue); }
  .corner-dark { fill: var(--brand-blue); }
</style>
</head>
<body>
<div class="sheet">
  <svg width="849" height="1200" viewBox="0 0 849 1200" xmlns="http://www.w3.org/2000/svg">
    <!-- brand -->
    <circle class="brand-dot" cx="82" cy="104" r="22"/>
    <text class="brand-name" x="120" y="127" font-size="62">HARROW VT</text>

    <!-- background panels -->
    <path class="panel-grey" d="M0 187 H290 C340 187 395 225 372 275 L0 1020 Z"/>
    <path class="band" d="M0 233 H849 V520 L808 600 C795 625 770 627 745 627 H0 Z"/>
    <path class="band-overlap" d="M0 233 H360 C380 245 385 260 372 275 L196 627 H0 Z"/>

    <!-- title -->
    <text class="title-years" x="71" y="302" font-size="40">2024 - 2025</text>
    <text class="title-financial" x="66" y="404" font-size="118" textLength="673">FINANCIAL</text>
    <text class="title-year" x="68" y="588" font-size="231" textLength="682">YEAR</text>

    <!-- stats -->
    <circle class="stat-ring" cx="347" cy="735" r="83"/>
    <circle class="stat-disc" cx="225" cy="735" r="58"/>
    <text class="stat-value" x="225" y="747" font-size="33">18M</text>
    <text class="stat-light" x="353" y="731" font-size="22">Annual</text>
    <text class="stat-bold" x="353" y="754" font-size="22">Turnover</text>

    <circle class="stat-ring" cx="688" cy="735" r="84"/>
    <circle class="stat-disc" cx="568" cy="735" r="57"/>
    <text class="stat-value" x="569" y="746" font-size="31">52%</text>
    <text class="stat-light" x="696" y="731" font-size="23">Conversion</text>
    <text class="stat-bold" x="694" y="762" font-size="31">Rate</text>

    <circle class="stat-ring" cx="262" cy="923" r="83"/>
    <circle class="stat-disc" cx="149" cy="923" r="50"/>
    <text class="stat-value" x="148" y="933" font-size="28">21%</text>
    <text class="stat-bold" x="264" y="943" font-size="58">GP</text>

    <circle class="stat-ring" cx="595" cy="921" r="84"/>
    <circle class="stat-disc" cx="473" cy="921" r="50"/>
    <text class="stat-value" x="473" y="932" font-size="30">200</text>
    <text class="stat-light" x="602" y="917" font-size="17">Average Quotes</text>
    <text class="stat-bold" x="601" y="939" font-size="17">Per Week</text>

    <circle class="stat-ring" cx="415" cy="1089" r="84"/>
    <circle class="stat-disc" cx="296" cy="1089" r="50"/>
    <text class="stat-value" x="296" y="1100" font-size="29">10%</text>
    <text class="stat-light" x="422" y="1083" font-size="18">Annual Growth</text>
    <text class="stat-bold" x="416" y="1107" font-size="24">Rate</text>

    <!-- corner accents -->
    <path class="corner-light" d="M849 830 V1070 H765 C740 1070 722 1055 730 1040 Z"/>
    <path class="corner-dark" d="M849 898 V1200 H698 Z"/>
  </svg>
</div>
</body>
</html>
```